Business Card Design Project

This is to go hand in hand with our stationery project.
Target Market(s)
Business Professionals in the Finance, HR and C-Level management arena. They are global companies that run enterprise technology solutions/products.
Mostly Male, mid 30's to 60's.
Industry/Entity Type
Business
Font styles to use
Other font styles liked:
- Calibri
Colors
9bcb3c
000000
1b1b1b
c4c4c4
ffffff
Requirements
Must have
- Logo
Name, title, contact details, address on the front of the card.
ABN and web address need to be on the card, along with our tag line
See | Share | Do
We also require rounded corners and for the card to be landscape please.
Our green is
C98 M0 Y93 K0
Modern, contemporary and must have white space for people to write on.
Nice to have
- Consistent elements with the stationery design.
Should not have
- No 90's waves - We want the feeling of movement but no wavey lines.

```html
<!DOCTYPE html>
<html lang="en">
<head>
<meta charset="utf-8">
<title>Nexa Business Solutions – Business Card</title>
<link href="https://fonts.googleapis.com/css2?family=Carlito:wght@400;700&display=swap" rel="stylesheet">
<style>
  :root {
    --green: #9bcb3c;
    --black: #000000;
    --ink: #1b1b1b;
    --grey: #c4c4c4;
    --white: #ffffff;
    --edge: #9a9a9a;
  }
  * { box-sizing: border-box; margin: 0; padding: 0; }
  html, body {
    width: 1200px; height: 369px; overflow: hidden;
    background: var(--white);
    font-family: "Carlito", "Calibri", sans-serif;
    color: var(--black);
  }
  .canvas { position: relative; width: 1200px; height: 369px; }
  .card {
    position: absolute; top: 3px; width: 581px; height: 362px;
    border: 1px solid var(--edge); border-radius: 9px; overflow: hidden;
  }
  /* Back of card */
  .card--back { left: 3px; background: var(--grey); }
  .brand {
    position: absolute; left: 0; right: 0; top: 92px;
    text-align: center; color: var(--ink); font-weight: 700;
  }
  .brand__name { font-size: 64px; line-height: 1; letter-spacing: 2px; }
  .brand__name .brand__dot {
    display: inline-block; width: 14px; height: 14px; border-radius: 50%;
    background: var(--ink); margin-left: 8px; vertical-align: middle;
  }
  .brand__sub { font-size: 23px; line-height: 1.3; margin-top: 6px; }
  .tagline { font-size: 15px; letter-spacing: .3px; }
  .tagline .sep { color: var(--green); margin: 0 6px; }
  .card--back .tagline {
    position: absolute; left: 0; right: 0; top: 218px; text-align: center;
  }
  .footer-band {
    position: absolute; left: 0; right: 0; bottom: 0; height: 31px;
    background: var(--green); font-size: 8px; color: var(--ink);
  }
  .footer-band span { position: absolute; top: 11px; white-space: nowrap; }

  /* Front of card */
  .card--front { left: 614px; background: var(--white); }
  .card--front .slant { position: absolute; inset: 0; width: 100%; height: 100%; }
  .mini-brand {
    position: absolute; left: 6px; top: 6px; color: var(--ink); font-weight: 700;
  }
  .mini-brand__name { font-size: 34px; line-height: 1; letter-spacing: 1px; }
  .mini-brand__sub { font-size: 13.5px; line-height: 1.2; margin-top: 3px; }
  .card--front .tagline { position: absolute; left: 27px; top: 87px; font-size: 10px; }
  .card--front .tagline .sep { margin: 0 4px; }
  .contact { position: absolute; font-size: 11px; color: var(--black); white-space: nowrap; }
  .contact--name { left: 364px; top: 111px; font-size: 12.5px; font-weight: 700; }
  .contact--title { left: 370px; top: 139px; font-size: 10.5px; }
  .contact--phone { left: 376px; top: 164px; display: flex; align-items: center; gap: 7px; }
  .contact--email { left: 384px; top: 191px; display: flex; align-items: center; gap: 7px; }
  .contact svg { display: block; }
</style>
</head>
<body>
<div class="canvas">

  <section class="card card--back">
    <div class="brand">
      <div class="brand__name">NEXA<span class="brand__dot"></span></div>
      <div class="brand__sub">Business Solutions</div>
    </div>
    <div class="tagline">See<span class="sep">•</span>Share<span class="sep">•</span>Do</div>
    <div class="footer-band">
      <span style="left:71px">T: +61 2 9000 1234</span>
      <span style="left:186px">F: +61 2 9000 5678</span>
      <span style="left:306px">www.nexabusiness.com</span>
      <span style="left:452px">ABN: 12 345 678 901</span>
    </div>
  </section>

  <section class="card card--front">
    <svg class="slant" viewBox="0 0 581 362" preserveAspectRatio="none" aria-hidden="true">
      <polygon points="245,0 581,0 581,362 336,362" fill="var(--green)"/>
    </svg>
    <div class="mini-brand">
      <div class="mini-brand__name">NEXA</div>
      <div class="mini-brand__sub">Business Solutions</div>
    </div>
    <div class="tagline">See<span class="sep">•</span>Share<span class="sep">•</span>Do</div>

    <div class="contact contact--name">Daniel Hart</div>
    <div class="contact contact--title">General Manager</div>
    <div class="contact contact--phone">
      <svg width="10" height="10" viewBox="0 0 24 24" aria-hidden="true">
        <path fill="var(--ink)" d="M6.6 10.8a15.1 15.1 0 0 0 6.6 6.6l2.2-2.2a1 1 0 0 1 1-.25 11.4 11.4 0 0 0 3.6.57 1 1 0 0 1 1 1V20a1 1 0 0 1-1 1A17 17 0 0 1 3 4a1 1 0 0 1 1-1h3.5a1 1 0 0 1 1 1c0 1.25.2 2.45.57 3.57a1 1 0 0 1-.25 1z"/>
      </svg>
      <span>0300 555 014</span>
    </div>
    <div class="contact contact--email">
      <svg width="12" height="9" viewBox="0 0 24 18" aria-hidden="true">
        <rect x="0" y="0" width="24" height="18" fill="var(--ink)"/>
        <polyline points="1,1 12,10 23,1" fill="none" stroke="var(--green)" stroke-width="2"/>
      </svg>
      <span>daniel.hart@nexabusiness.com</span>
    </div>
  </section>

</div>
</body>
</html>
```